Real Estate Templates in Canva

I need someone to create a robust set of Canva template designs for my real estate company team, to streamline content. I need a catalog for my agents to easily go in and pick from different designs and customize for themselves. The correct candidate can emulate the style found on these sites., and in the attached images. I have also uploaded logos to be used.(https://www.brindlehomegroup.com/) and (https://meetkoravel.com/)

I want a fantastic sharp style that has great color blend and is attractive and matches my brand well.

The correct candidate will have access to my Canva Brand Kit and build templates inside of my account.

Also attached is a screenshot of my main color codes

The types of templates can include, but not be limited to the following:
BOTH DIGITAL FOR SOCIAL MEDIA AND PRINT VERSIONS
Listings flyers
Clients testimonials
market stats
open houses
Realtor Insights
Realtor analysis
sold properties
new listing properties
under contract properties
coming soon properties
Bullet points summarizing key data
Photo of the client at closing
Photo of the client at their home

Property Listing Template:

Description of the property
High-quality images
Key features and amenities
Open House Invitation:

Date, time, and location details
Compelling visuals of the property
Call-to-action for attendance
Just Sold Announcement:

Property details (address, price, etc.)
Celebratory message
Testimonials from satisfied clients
Testimonial Template:

Client testimonial
Photo of the client (with permission)
Brief background or story
Market Update Infographic:

Visual representation of current market trends
Realtor's insights and analysis
Buyer's Guide:

Step-by-step guide for homebuyers
Infographics explaining the buying process
Tips and advice for a successful purchase
Seller's Guide:

Information on preparing a home for sale
Infographics on the selling process
Tips for maximizing property value
Seasonal Greetings Template:

Personalized message for clients
Festive visuals or themes
Wishes for a successful year ahead
Neighborhood Highlight:

Showcase a specific neighborhood
Key attractions, schools, amenities
Testimonials from residents (if available)
Behind-the-Scenes:

Photos or videos of the realtor at work
Personalized messages about the real estate process
Humanizing content to connect with the audience
Infographic: Benefits of Working with a Realtor:

Visual representation of the advantages
Statistics or data supporting the benefits
Clear, concise points for easy consumption
Interactive Polls or Quizzes:

Engage the audience with fun polls
Real estate-related quizzes
Encourage interaction and sharing
Client Appreciation Post:

Thanking clients for their trust
Sharing success stories
Expressing gratitude with visuals
Video Tour Teaser:

Sneak peek of a property tour
Create excitement and anticipation

Target Market(s)

General Population ages 30-70

Requirements
Must have
• 60 plus designs
Nice to have
• 100 plus designs

```html
<!DOCTYPE html>
<html lang="en">
<head>
<meta charset="utf-8">
<title>Brindle Home Group – Featured Listings Flyer</title>
<link rel="stylesheet" href="https://fonts.googleapis.com/css2?family=Jost:wght@400;600&family=Montserrat:wght@400;600;800&display=swap">
<style>
  :root {
    --brand-orange: #F39431;
    --brand-black: #151515;
    --paper: #ffffff;
    --backdrop: #efefef;
    --ink: #1c1c1c;
  }
  * { box-sizing: border-box; margin: 0; padding: 0; }
  html, body { width: 759px; height: 1200px; overflow: hidden; }
  body { background: var(--backdrop); position: relative; font-family: "Montserrat", sans-serif; color: var(--ink); }

  .flyer-page {
    position: absolute;
    left: 176px;
    width: 497px;
    height: 702px;
    background: var(--paper);
    overflow: hidden;
    transform: scale(0.8209);
    transform-origin: top left;
  }
  .flyer-page--cover { top: 16px; }
  .flyer-page--listing { top: 608px; }

  .page-shapes { position: absolute; inset: 0; width: 497px; height: 702px; }

  .brand-mark {
    position: absolute;
    display: flex;
    align-items: center;
    gap: 7px;
  }
  .brand-mark__dot { width: 28px; height: 28px; border-radius: 50%; background: var(--brand-black); flex: none; }
  .brand-mark__name {
    font-family: "Montserrat", sans-serif;
    font-weight: 600;
    font-size: 14px;
    line-height: 1;
    color: var(--brand-orange);
    white-space: nowrap;
  }
  .flyer-page--cover .brand-mark { left: 290px; top: 44px; }
  .flyer-page--listing .brand-mark { left: 43px; top: 45px; }

  .cover-title {
    position: absolute;
    left: 42px;
    top: 72px;
    font-family: "Montserrat", sans-serif;
    font-weight: 800;
    font-size: 35px;
    line-height: 37px;
    color: var(--paper);
    text-transform: uppercase;
  }

  .topic-list {
    position: absolute;
    left: 42px;
    top: 337px;
    list-style: none;
    font-size: 14px;
    line-height: 20.85px;
  }
  .topic-list::before {
    content: "";
    position: absolute;
    left: 2px;
    top: 10px;
    bottom: 10px;
    width: 1px;
    background: var(--brand-orange);
  }
  .topic-list__item { position: relative; padding-left: 15px; white-space: nowrap; }
  .topic-list__item::before {
    content: "";
    position: absolute;
    left: 0;
    top: 8px;
    width: 5px;
    height: 5px;
    border-radius: 50%;
    background: var(--brand-orange);
  }

  .site-url {
    position: absolute;
    font-family: "Jost", sans-serif;
    font-size: 14px;
    color: var(--ink);
  }
  .flyer-page--cover .site-url { left: 42px; top: 638px; }
  .flyer-page--listing .site-url { left: 0; right: 0; top: 655px; text-align: center; font-size: 16px; }

  .template-brief {
    position: absolute;
    left: 42px;
    top: 107px;
    font-family: "Jost", sans-serif;
    font-size: 15px;
    line-height: 21px;
  }
  .template-brief__heading { font-weight: 600; }
</style>
</head>
<body>

  <section class="flyer-page flyer-page--cover">
    <svg class="page-shapes" viewBox="0 0 497 702">
      <defs>
        <linearGradient id="summitSky" x1="0" y1="0" x2="0" y2="1">
          <stop offset="0" stop-color="#8fb1c2"/>
          <stop offset="0.45" stop-color="#c9c6a8"/>
          <stop offset="0.62" stop-color="#e9b96a"/>
          <stop offset="0.8" stop-color="#3b3128"/>
          <stop offset="1" stop-color="#1d1915"/>
        </linearGradient>
      </defs>
      <polygon points="0,0 153,0 312,102 172,300 0,200" fill="var(--brand-orange)"/>
      <g role="img" aria-label="Photo of two hikers celebrating on a mountain summit at sunset">
        <polygon points="312,102 497,215 497,500 172,300" fill="url(#summitSky)"/>
      </g>
      <polygon points="340,600 340,578 478,495 497,495 497,505" fill="var(--brand-black)"/>
      <polygon points="170,702 497,505 497,702" fill="var(--brand-orange)"/>
    </svg>

    <div class="brand-mark">
      <span class="brand-mark__dot"></span>
      <span class="brand-mark__name">Brindle Home Group</span>
    </div>

    <h1 class="cover-title">Our<br>Featured<br>Listings</h1>

    <ul class="topic-list">
      <li class="topic-list__item">Clients testimonials</li>
      <li class="topic-list__item">Market stats</li>
      <li class="topic-list__item">Open houses</li>
      <li class="topic-list__item">Realtor Insights</li>
      <li class="topic-list__item">Realtor analysis</li>
      <li class="topic-list__item">Dold properties</li>
      <li class="topic-list__item">New listing properties</li>
      <li class="topic-list__item">Under contract properties</li>
      <li class="topic-list__item">Coming soon properties</li>
      <li class="topic-list__item">Bullet points summarizing key data</li>
      <li class="topic-list__item">Photo of the client at closing</li>
      <li class="topic-list__item">Photo of the client at their home</li>
    </ul>

    <p class="site-url">www.brindlehomegroup.com</p>
  </section>

  <section class="flyer-page flyer-page--listing">
    <svg class="page-shapes" viewBox="0 0 497 702">
      <defs>
        <linearGradient id="valleyTones" x1="0" y1="0" x2="0" y2="1">
          <stop offset="0" stop-color="#9fb9d4"/>
          <stop offset="0.45" stop-color="#6f7f55"/>
          <stop offset="1" stop-color="#b9a47c"/>
        </linearGradient>
        <linearGradient id="pineTones" x1="0" y1="0" x2="0" y2="1">
          <stop offset="0" stop-color="#a9bccb"/>
          <stop offset="0.5" stop-color="#4f5b3c"/>
          <stop offset="1" stop-color="#8a8470"/>
        </linearGradient>
        <linearGradient id="snowTones" x1="0" y1="0" x2="0" y2="1">
          <stop offset="0" stop-color="#8d8fa3"/>
          <stop offset="0.35" stop-color="#d9a27a"/>
          <stop offset="0.6" stop-color="#6b5648"/>
          <stop offset="1" stop-color="#dfe3ea"/>
        </linearGradient>
        <linearGradient id="meadowTones" x1="0" y1="0" x2="0" y2="1">
          <stop offset="0" stop-color="#5d8fc9"/>
          <stop offset="0.35" stop-color="#dfe8f0"/>
          <stop offset="0.6" stop-color="#4f6b3a"/>
          <stop offset="1" stop-color="#7ea24c"/>
        </linearGradient>
        <linearGradient id="cabinTones" x1="0" y1="0" x2="0" y2="1">
          <stop offset="0" stop-color="#6e5237"/>
          <stop offset="0.6" stop-color="#8b6a48"/>
          <stop offset="1" stop-color="#6fa33c"/>
        </linearGradient>
        <linearGradient id="prairieTones" x1="0" y1="0" x2="0" y2="1">
          <stop offset="0" stop-color="#b7c6d8"/>
          <stop offset="0.3" stop-color="#8a8a74"/>
          <stop offset="1" stop-color="#a78761"/>
        </linearGradient>
      </defs>

      <polygon points="148,0 202,0 175,20" fill="var(--brand-black)"/>
      <polygon points="212,0 302,0 262,38" fill="var(--brand-orange)"/>
      <polygon points="287,0 342,0 398,55 362,82" fill="var(--brand-black)"/>
      <polygon points="342,0 497,0 497,74 472,104" fill="var(--brand-orange)"/>

      <g fill="none" stroke="var(--brand-orange)" stroke-width="1.6">
        <polyline points="185,240 180,337"/>
        <polyline points="328,240 323,337"/>
        <polyline points="482,240 477,337 470,337"/>
        <polyline points="182,361 177,458 37,458 40,440"/>
        <polyline points="325,361 320,458 180,458 183,440"/>
        <polyline points="468,361 463,458 323,458 326,440"/>
      </g>

      <g role="img" aria-label="Listing photo: mountain valley with pine forest and cabin">
        <polygon points="45,215 182,215 178,313 41,313" fill="url(#valleyTones)"/>
      </g>
      <g role="img" aria-label="Listing photo: pine trees along a quiet road">
        <polygon points="188,215 326,215 322,313 184,313" fill="url(#pineTones)"/>
      </g>
      <g role="img" aria-label="Listing photo: home in snow at sunset">
        <polygon points="330,215 470,215 466,313 326,313" fill="url(#snowTones)"/>
      </g>
      <g role="img" aria-label="Listing photo: green meadow with mountain views">
        <polygon points="31,336 171,336 167,434 27,434" fill="url(#meadowTones)"/>
      </g>
      <g role="img" aria-label="Listing photo: log cabin with a lawn">
        <polygon points="174,336 314,336 310,434 170,434" fill="url(#cabinTones)"/>
      </g>
      <g role="img" aria-label="Listing photo: open prairie land with dry grass">
        <polygon points="317,336 457,336 453,434 313,434" fill="url(#prairieTones)"/>
      </g>

      <polygon points="212,540 242,513 333,590 303,614" fill="var(--brand-black)"/>
      <polygon points="398,592 420,572 497,638 497,672" fill="var(--brand-black)"/>
      <polygon points="0,622 150,489 303,614 352,557 497,675 497,702 0,702" fill="var(--brand-orange)"/>
    </svg>

    <div class="brand-mark">
      <span class="brand-mark__dot"></span>
      <span class="brand-mark__name">Brindle Home Group</span>
    </div>

    <div class="template-brief">
      <p class="template-brief__heading">Property Listing Template:</p>
      <p>Description of the property</p>
      <p>High-quality images</p>
      <p>Key features and amenities</p>
    </div>

    <p class="site-url">www.brindlehomegroup.com</p>
  </section>

</body>
</html>
```